Meridian Sound Wellness LLC Card Design

Need business card with a logo for a hearing aid sales and audiology business. We have two Hearing Instrument Specialists and one Audiologist on staff. Over 25 years in business. Locally owned and operated. Financing available. Most insurances accepted.

Meridian Sound Wellness LLC
48730 W Linden Row, Suite 9
Spokane, WA 99481
509-617-2085
www.meridiansoundnorth.example

Manager
Tobias Wrenfield HIS COHC
License #81729046

Target Market(s)

50yr old + people with a hearing loss.

Industry/Entity Type

Business

Contact Information for Business Card

48730 W Linden Row, Suite 9
Spokane, WA 99481
509-617-2085
www.meridiansoundnorth.example

Manager
Tobias Wrenfield HIS COHC
NRPL #81729046

Font styles to use
Serif
Sans Serif

Requirements
Must have
• Business name, Tobias's name and title(s) and contact information, License #, web address
Nice to have
Should not have

```html
<!DOCTYPE html>
<html lang="en">
<head>
<meta charset="utf-8">
<title>Meridian Sound Wellness – Business Card</title>
<link rel="stylesheet" href="https://fonts.googleapis.com/css2?family=Cinzel:wght@400;500&display=swap">
<style>
  :root {
    --backdrop: #d6d6d6;
    --card-black: #231f20;
    --lime: #8dc63f;
    --lime-light: #b5e061;
    --lime-dark: #6fa52a;
    --white: #f2f2f2;
    --ink: #1d1d1b;
  }
  html, body {
    margin: 0;
    width: 1200px;
    height: 800px;
    overflow: hidden;
    background: var(--backdrop);
    font-family: "Cinzel", "Trajan Pro", serif;
  }
  .canvas {
    position: relative;
    width: 1200px;
    height: 800px;
  }
  .card {
    position: absolute;
    left: 100px;
    top: 115px;
    width: 1000px;
    height: 570px;
    border-radius: 42px;
    background: var(--card-black);
    overflow: hidden;
    box-shadow: 0 18px 40px rgba(0,0,0,0.25);
  }
  .brand {
    position: absolute;
    left: 90px;
    top: 95px;
    width: 320px;
  }
  .brand-dot {
    display: block;
    width: 104px;
    height: 104px;
    border-radius: 50%;
    background: var(--lime);
    margin: 0 0 22px 18px;
  }
  .brand-name {
    display: block;
    color: var(--white);
    font-size: 30px;
    font-weight: 400;
    line-height: 1.2;
    letter-spacing: 1.5px;
  }
  .person {
    position: absolute;
    right: 80px;
    top: 222px;
    text-align: right;
  }
  .person-line {
    font-size: 34px;
    line-height: 1.1;
  }
  .person-name { color: var(--lime); }
  .person-cred { color: var(--white); font-size: 28px; margin-left: 10px; }
  .person-role {
    color: var(--white);
    font-size: 26px;
    margin-top: 2px;
  }
  .divider {
    position: absolute;
    left: 90px;
    right: 80px;
    top: 338px;
    height: 2px;
    background: var(--lime-dark);
  }
  .contact {
    position: absolute;
    left: 90px;
    top: 362px;
    font-size: 27px;
    line-height: 1.5;
    color: var(--white);
  }
  .contact .value { color: var(--lime); }
  .address {
    position: absolute;
    right: 80px;
    top: 358px;
    text-align: right;
    font-size: 29px;
    line-height: 1.35;
    color: var(--lime);
  }
  .web-band {
    position: absolute;
    left: 0;
    right: 0;
    bottom: 0;
    height: 92px;
    background: linear-gradient(180deg, var(--lime-light) 0%, var(--lime) 45%, var(--lime-dark) 100%);
  }
  .web-rule {
    position: absolute;
    left: 0;
    width: 340px;
    top: 14px;
    height: 2px;
    background: var(--card-black);
    opacity: 0.55;
  }
  .web {
    position: absolute;
    right: 80px;
    top: 12px;
    display: flex;
    align-items: center;
    gap: 12px;
    color: var(--ink);
    font-size: 27px;
    letter-spacing: 0.5px;
  }
  .web svg { width: 26px; height: 26px; }
</style>
</head>
<body>
<div class="canvas">
  <div class="card">
    <div class="brand">
      <span class="brand-dot"></span>
      <span class="brand-name">Meridian Sound<br>Wellness</span>
    </div>

    <div class="person">
      <div class="person-line"><span class="person-name">Tobias Wrenfield</span><span class="person-cred">HIS COHC</span></div>
      <div class="person-role">Manager</div>
    </div>

    <div class="divider"></div>

    <div class="contact">
      <div>Ph: <span class="value">509-617-2085</span></div>
      <div>NRPL: <span class="value">#81729046</span></div>
    </div>

    <div class="address">
      <div>48730 W Linden Row, Suite 9</div>
      <div>Spokane, WA 99481</div>
    </div>

    <div class="web-band">
      <div class="web-rule"></div>
      <div class="web">
        <svg viewBox="0 0 24 24" aria-hidden="true">
          <circle cx="12" cy="12" r="10.5" fill="none" stroke="#1d1d1b" stroke-width="2"/>
          <ellipse cx="12" cy="12" rx="4.5" ry="10.5" fill="none" stroke="#1d1d1b" stroke-width="1.5"/>
          <line x1="1.5" y1="12" x2="22.5" y2="12" stroke="#1d1d1b" stroke-width="1.5"/>
        </svg>
        <span>www.meridiansoundnorth.example</span>
      </div>
    </div>
  </div>
</div>
</body>
</html>
```